International Film making Business needs the 5 Logos provided made into a POSTER Format

Design Task:
CREATE A POSTER DESIGN USING THE 5 LOGOS PROVIDED. The GLAD SKY VISTA LOGO should stand out from the others by being in the middle with the other 4 logos connected to it somehow.

The 5 Businesses already has their 5 Logos, all similar in design to each other.

GLAD SKY VISTA is the Main Logo that encompasses the other 4 Logos. So it must stand out more and it is like the Overall Business entity that incorporates the other 4 Logos.

What is required is that by using the 5 Logo designs provided, create a cool graphic artwork that somehow incorporates ALL of the 5 Logos - But having the GLAD SKY VISTA Logo at the forefront/most important/standing out the most.
- GLAD SKY VISTA will probably be bigger than the others
- and could be changed into 3D.

I have attached all 5 logos and a hand drawn example of how the GLAD SKY VISTAS could stand out from the rest.

THE DESIGNS OF THE LOGOS SHOULD NOT BE CHANGED (except the GLADSKYVISTA which can be 3D)

Please do not be restricted with the sample idea. Creativity is encouraged

DIMENSION: 3000 mm x 6000 mm
high resolution graphic

Logo Text

glad sky , glad sky reels, glad sky tales, glad sky groovy, GLAD SKY VISTAS

Requirements
Must have
• USE THE 5 LOGOS PROVIDED ONLY - Only GLAD SKY VISTA can be changed into 3D only
Nice to have
• Eye catching design, showing the Glad Sky Vista as the most powerful Logo that has the other 4 as subordinate companies
Should not have
• ANY CHANGE IN THE 5 LOGO DESIGNS (EXcept 3D for Glad Sky Vistas)

```html
<!DOCTYPE html>
<html lang="en">
<head>
<meta charset="utf-8">
<title>Glad Sky Vistas – Group Poster</title>
<link rel="stylesheet" href="https://fonts.googleapis.com/css2?family=Cinzel:wght@500;600;700&family=Montserrat:wght@300&display=swap">
<style>
  :root {
    --gold-dark: #b07d2a;
    --gold-mid: #d8b35e;
    --gold-light: #f7eab0;
    --ink: #000000;
    --paper: #ffffff;
    --url-grey: #9a9a9a;
    --blue: #1c7fc6;
    --reels-grey: #2b2b2b;
    --tales-purple: #5b2d8e;
    --groovy-green: #1f8a3a;
  }
  html, body {
    margin: 0;
    padding: 0;
    width: 1200px;
    height: 600px;
    overflow: hidden;
    background: var(--paper);
  }
  .poster {
    display: block;
    width: 1200px;
    height: 600px;
  }
  .brand-title {
    font-family: "Cinzel", serif;
    font-weight: 600;
    fill: var(--gold-mid);
    letter-spacing: 4px;
  }
  .brand-url {
    font-family: "Montserrat", sans-serif;
    font-weight: 300;
    fill: var(--url-grey);
    letter-spacing: 5px;
  }
  .sub-name {
    font-family: "Cinzel", serif;
    font-weight: 600;
  }
  .sub-name--sky { fill: var(--blue); }
  .sub-name--reels { fill: var(--reels-grey); }
  .sub-name--tales { fill: var(--tales-purple); }
  .sub-name--groovy { fill: var(--groovy-green); }
</style>
</head>
<body>
<svg class="poster" viewBox="0 0 1200 600" xmlns="http://www.w3.org/2000/svg">
  <defs>
    <linearGradient id="gold-frame" x1="0" y1="0" x2="1" y2="0">
      <stop offset="0" stop-color="#b07d2a"/>
      <stop offset="0.3" stop-color="#d8b35e"/>
      <stop offset="0.55" stop-color="#f7eab0"/>
      <stop offset="0.8" stop-color="#c9993f"/>
      <stop offset="1" stop-color="#b07d2a"/>
    </linearGradient>
    <linearGradient id="gold-diamond" x1="0" y1="0" x2="1" y2="1">
      <stop offset="0" stop-color="#b07d2a"/>
      <stop offset="0.35" stop-color="#f7eab0"/>
      <stop offset="0.6" stop-color="#b07d2a"/>
      <stop offset="0.85" stop-color="#f7eab0"/>
      <stop offset="1" stop-color="#b07d2a"/>
    </linearGradient>
    <linearGradient id="band-blue" x1="0" y1="0" x2="1" y2="0">
      <stop offset="0" stop-color="#2a3f93"/>
      <stop offset="0.55" stop-color="#1ab0e6"/>
      <stop offset="1" stop-color="#2a3f93"/>
    </linearGradient>
    <linearGradient id="band-grey" x1="0" y1="0" x2="1" y2="0">
      <stop offset="0" stop-color="#0c0c0c"/>
      <stop offset="0.55" stop-color="#8a8a8a"/>
      <stop offset="1" stop-color="#0c0c0c"/>
    </linearGradient>
    <linearGradient id="band-rainbow" x1="0" y1="0" x2="1" y2="0">
      <stop offset="0" stop-color="#6a2f94"/>
      <stop offset="0.25" stop-color="#2a3f93"/>
      <stop offset="0.5" stop-color="#1ab0e6"/>
      <stop offset="0.68" stop-color="#3cb44a"/>
      <stop offset="0.85" stop-color="#fff200"/>
      <stop offset="1" stop-color="#f26522"/>
    </linearGradient>
    <linearGradient id="band-green" x1="0" y1="0" x2="1" y2="0">
      <stop offset="0" stop-color="#0b6e3a"/>
      <stop offset="0.55" stop-color="#8cc63f"/>
      <stop offset="1" stop-color="#0b6e3a"/>
    </linearGradient>
    <radialGradient id="emblem-fill" cx="0.4" cy="0.35" r="0.7">
      <stop offset="0" stop-color="#f7eab0"/>
      <stop offset="1" stop-color="#b07d2a"/>
    </radialGradient>
  </defs>

  <!-- outer frame -->
  <rect class="frame" x="0" y="0" width="1200" height="600" fill="url(#gold-frame)"/>

  <!-- header panel -->
  <rect class="header-panel" x="18" y="18" width="1164" height="262" fill="var(--ink)"/>
  <circle class="brand-emblem" cx="420" cy="150" r="78" fill="url(#emblem-fill)"/>
  <text class="brand-title" x="523" y="162" font-size="72" textLength="387" lengthAdjust="spacingAndGlyphs">GLAD SKY</text>
  <text class="brand-title" x="523" y="232" font-size="72" textLength="387" lengthAdjust="spacingAndGlyphs">VISTAS</text>
  <text class="brand-url" x="523" y="264" font-size="25" textLength="387" lengthAdjust="spacingAndGlyphs">gladskyvistas.com.au</text>

  <!-- division bands -->
  <rect class="band" x="18" y="280" width="303" height="302" fill="url(#band-blue)"/>
  <rect class="band" x="321" y="280" width="275" height="302" fill="url(#band-grey)"/>
  <rect class="band" x="596" y="280" width="280" height="302" fill="url(#band-rainbow)"/>
  <rect class="band" x="876" y="280" width="306" height="302" fill="url(#band-green)"/>

  <!-- division diamonds -->
  <g class="diamond">
    <polygon points="182,283 331,431 182,579 33,431" fill="url(#gold-diamond)"/>
    <polygon points="182,301 313,431 182,561 51,431" fill="var(--paper)"/>
  </g>
  <g class="diamond">
    <polygon points="460,283 609,431 460,579 311,431" fill="url(#gold-diamond)"/>
    <polygon points="460,301 591,431 460,561 329,431" fill="var(--paper)"/>
  </g>
  <g class="diamond">
    <polygon points="739,283 888,431 739,579 590,431" fill="url(#gold-diamond)"/>
    <polygon points="739,301 870,431 739,561 608,431" fill="var(--paper)"/>
  </g>
  <g class="diamond">
    <polygon points="1020,283 1169,431 1020,579 871,431" fill="url(#gold-diamond)"/>
    <polygon points="1020,301 1151,431 1020,561 889,431" fill="var(--paper)"/>
  </g>

  <!-- division names -->
  <g class="division">
    <circle cx="124" cy="425" r="20" fill="var(--blue)"/>
    <text class="sub-name sub-name--sky" x="170" y="428" font-size="34">GLAD</text>
    <text class="sub-name sub-name--sky" x="170" y="462" font-size="34">SKY</text>
  </g>
  <g class="division">
    <circle cx="394" cy="425" r="20" fill="var(--reels-grey)"/>
    <text class="sub-name sub-name--reels" x="432" y="425" font-size="22">GLAD SKY</text>
    <text class="sub-name sub-name--reels" x="432" y="455" font-size="30">REELS</text>
  </g>
  <g class="division">
    <circle cx="672" cy="425" r="20" fill="var(--tales-purple)"/>
    <text class="sub-name sub-name--tales" x="708" y="425" font-size="22">GLAD SKY</text>
    <text class="sub-name sub-name--tales" x="708" y="455" font-size="30">TALES</text>
  </g>
  <g class="division">
    <circle cx="1020" cy="395" r="22" fill="var(--groovy-green)"/>
    <text class="sub-name sub-name--groovy" x="1020" y="460" font-size="24" text-anchor="middle">GLAD SKY</text>
    <text class="sub-name sub-name--groovy" x="1020" y="492" font-size="30" text-anchor="middle">GROOVY</text>
  </g>
</svg>
</body>
</html>
```